Website - Tides Of Motion

We are catalysts of change in people's lives.
We work with individuals and professionals to bring about instant substantial & transforming change in their lives.
We provide one-on-one lifestyle coaching by an experienced practitioner.
Our existing website is www.tidesofmotion.biz & this site contains our the basis for the content of our desired new project, so please examine this carefully.
We require a professional and captivating website that will instantly impress, engage invite our readers to click & invest their lives.
Our services do not come cheap, but are second to none.
Our website must be contemporary whilst reflecting indisputable class & ultra-confidence in the success of our work.
Target Market(s)
Those who seek to want to change in their lives. Those aged primarily between 30 and 50 years of age, male or female.
Industry/Entity Type
Work

```html
<!DOCTYPE html>
<html lang="en">
<head>
<meta charset="utf-8">
<title>Tides Of Motion</title>
<link href="https://fonts.googleapis.com/css2?family=Cabin:wght@400;500&family=Raleway:wght@400&family=Roboto:wght@400;500;700&display=swap" rel="stylesheet">
<style>
:root{
  --dark:#262d33;
  --panel-top:#58626c;
  --panel-bot:#3d454d;
  --nav:#505a63;
  --orange:#f08a1c;
  --body-bg:#ececec;
  --white:#ffffff;
  --ink:#222;
  --muted:#555;
  --blue:#4a6b86;
  --tick:#6aa33b;
}
*{box-sizing:border-box;margin:0;padding:0}
html,body{width:826px;height:1200px;overflow:hidden}
body{position:relative;background:var(--body-bg);font-family:"Roboto",Arial,sans-serif;color:var(--ink)}
.abs{position:absolute}
.header-band{left:0;top:0;width:826px;height:391px;background:var(--dark)}
.login{left:672px;top:0;width:44px;height:17px;background:#4a535b;color:#ddd;font-size:7.5px;font-weight:500;text-align:center;line-height:17px;letter-spacing:.4px}
.brand{left:111px;top:19px;width:172px;height:82px;background:#0a0a0a;display:flex;align-items:center;justify-content:center;gap:8px}
.brand-mark{width:14px;height:14px;background:var(--orange);border-radius:50%}
.brand-name{font-family:"Cabin",sans-serif;font-size:18px;color:#fff}
.call{right:110px;top:35px;color:#fff;font-size:9.5px;font-weight:700}
.nav{left:316px;top:54px;width:400px;height:27px;background:linear-gradient(#5a646d,#46505a);border-radius:2px;display:flex;align-items:center}
.nav a{color:#fff;font-size:7.5px;font-weight:700;text-decoration:none;letter-spacing:.3px;height:27px;line-height:27px;padding:0 24px;border-right:1px solid #3b444c}
.nav a:first-child{padding-left:25px}
.social{margin-left:auto;margin-right:10px;display:flex;gap:12px}
.social span{width:9px;height:9px;background:#8a939b;border-radius:1px}
.hero{left:111px;top:101px;width:605px;height:290px;background:linear-gradient(var(--panel-top),var(--panel-bot));border-radius:3px 3px 0 0}
.hero h1{left:136px;top:127px;width:270px;text-align:center;font-family:"Cabin",sans-serif;font-weight:400;font-size:23px;line-height:26px;color:#fff}
.hero-lead{left:136px;top:200px;width:275px;text-align:center;font-size:8px;line-height:14px;color:#f0f0f0;letter-spacing:.2px}
.rule{left:136px;top:281px;width:266px;height:1px;background:#6c7680}
.signup{left:205px;top:267px;width:131px;height:28px;background:var(--orange);border-radius:14px;color:#fff;font-size:10px;font-weight:700;text-align:center;line-height:28px}
.hero-story{left:136px;top:306px;width:280px;font-size:8px;line-height:12.4px;color:#eee;letter-spacing:.2px}
.slide{left:424px;top:127px;width:267px;height:154px;background:linear-gradient(135deg,#e9e9ea,#d7d2cf);border:1px solid #cfd3d6}
.arrows{left:424px;top:285px;display:flex;gap:3px}
.arrows svg{width:8px;height:8px}
.dots{left:648px;top:286px;display:flex;gap:6px}
.dots span{width:5px;height:5px;border-radius:50%;background:#fff}
.points{left:474px;top:306px;font-size:7.6px;font-weight:700;color:#fff;line-height:17.4px}
.content{left:111px;top:391px;width:605px;height:770px;background:var(--white)}
.col{width:180px;text-align:center}
.col h3{font-size:11.5px;font-weight:500;color:#111;margin-bottom:6px}
.col h4{font-size:7.6px;font-weight:700;color:#444;margin-bottom:14px}
.col p{font-size:7.4px;line-height:11.8px;color:#555;letter-spacing:.2px;padding:0 10px}
.ph{background:linear-gradient(#c8c8c8,#7b7b7b)}
.quote{left:136px;top:734px;font-family:"Raleway",sans-serif;font-size:16.5px;color:#222}
.cite{left:149px;top:762px;font-size:7.8px;color:#222}
.cite b{font-weight:700}
.section-title{font-family:"Raleway",sans-serif;font-size:14px;color:#222}
.why{left:136px;top:890px;width:180px;list-style:none}
.why li{position:relative;padding-left:15px;font-size:7.6px;line-height:9.3px;color:#333;margin-bottom:13px}
.why svg{position:absolute;left:0;top:0;width:10px;height:9px}
.post-title{left:438px;font-family:"Raleway",sans-serif;font-size:17px;line-height:20px;color:var(--blue)}
.meta{left:438px;font-size:6.6px;color:#555;display:flex;gap:10px;align-items:center}
.meta i{display:inline-block;width:7px;height:7px;border-radius:50%;background:#c6c6c6;margin-right:5px;vertical-align:middle}
.post-text{left:438px;width:255px;font-size:7.2px;line-height:11.5px;color:#333}
.pager{left:560px;top:1128px;display:flex;gap:4px}
.pager span{height:18px;line-height:18px;background:#222;color:#fff;font-size:8px;border-radius:2px;padding:0 6px}
.pager .on{background:#333;box-shadow:0 0 0 1px #3aa0d8}
.footer{left:0;top:1176px;width:826px;text-align:center;font-size:7px;color:#666}
</style>
</head>
<body>
<div class="abs header-band"></div>
<div class="abs login">LOGIN</div>
<div class="abs brand"><span class="brand-mark"></span><span class="brand-name">Tides Of Motion</span></div>
<div class="abs call">Call us on: +61 02 5550 1473</div>
<nav class="abs nav">
  <a>HOME</a><a>BUSINESS</a><a>INDIVIDUAL</a><a style="border-right:none">CONTACT</a>
  <div class="social"><span></span><span></span><span></span></div>
</nav>

<section class="abs hero"></section>
<h1 class="abs hero h1" style="position:absolute;left:136px;top:127px;width:270px;text-align:center;font-family:'Cabin',sans-serif;font-weight:400;font-size:23px;line-height:26px;color:#fff">Change begins today with our Master Practitioner</h1>
<p class="abs hero-lead">Our clients experience their desired instant &amp; permanent transformation, emerging from our consultations ready to take on their world from a vastly different paradigm</p>
<div class="abs rule"></div>
<div class="abs signup">SIGN UP HERE</div>
<p class="abs hero-story">At Tides Of Motion, our Master Practitioner will inspire you, shifting your perspective &amp; facilitating your mind with the freedom to realise your dreams<br>Join Ellis Warden, Martin Croft, R.L. Ashby, Dane Holloway, Nora Keyes, Lena Marsh and hundreds of thousands of others who are achieving the life changing, consistent results you are dreaming of now.</p>
<div class="abs slide" role="img" aria-label="Collage of client portrait photos"></div>
<div class="abs arrows">
  <svg viewBox="0 0 8 8"><circle cx="4" cy="4" r="4" fill="#fff"/><path d="M4.8 2 2.8 4l2 2" stroke="#333" stroke-width="1.2" fill="none"/></svg>
  <svg viewBox="0 0 8 8"><circle cx="4" cy="4" r="4" fill="#fff"/><path d="M3.2 2l2 2-2 2" stroke="#333" stroke-width="1.2" fill="none"/></svg>
</div>
<div class="abs dots"><span></span><span></span><span></span><span></span></div>
<div class="abs points">More choices about your behaviours and emotions<br>Improve your relationships and the ways you communicate<br>Create better results through becoming a greater thinker</div>

<main class="abs content"></main>

<div class="abs col" style="left:124px;top:431px">
  <h3>Business</h3><h4>Inspiring Business Excellence</h4>
  <p>Tides Of Motion have worked with CEO's &amp; business owners throughout Australia, as catalysts to their outstanding success.</p>
</div>
<div class="abs col" style="left:324px;top:431px">
  <h3>Individual</h3><h4>Individual Shift To An Outstanding Life</h4>
  <p>Tides Of Motion works every day with people just like you who wish to change their lives.</p>
</div>
<div class="abs col" style="left:522px;top:431px">
  <h3>Contact</h3><h4>You've waited long enough</h4>
  <p>Our studio comes with over 25 powerful shortcodes that all you to create amazing content in minutes.</p>
</div>
<div class="abs ph" style="left:135px;top:527px;width:161px;height:121px;background:linear-gradient(#e6e6e6,#5c5c5c)" role="img" aria-label="Black and white photo of two business people"></div>
<div class="abs ph" style="left:335px;top:527px;width:161px;height:120px;background:linear-gradient(#b7a999,#8e7a6c)" role="img" aria-label="Photo of two smiling young women"></div>
<div class="abs ph" style="left:534px;top:527px;width:157px;height:120px;background:linear-gradient(90deg,#e8d7c5,#c79b72,#fff)" role="img" aria-label="Photo of a support agent wearing a headset"></div>

<p class="abs quote">We're so excited by it and think its extraordinary!</p>
<p class="abs cite"><b>Rob Mills,</b>&nbsp; Lorem Ipsum</p>
<div class="abs" style="left:518px;top:675px;width:156px;height:138px;background:linear-gradient(#fff 0%,#e1bfa6 45%,#1f3350 70%)" role="img" aria-label="Portrait photo of a man in a navy shirt"></div>

<h2 class="abs section-title" style="left:136px;top:858px;font-weight:400">Why Us?</h2>
<h2 class="abs section-title" style="left:341px;top:858px;font-weight:400">From The Blog</h2>

<ul class="abs why">
  <li><svg viewBox="0 0 10 9"><path d="M1 5l3 3 5-7" stroke="var(--tick)" stroke-width="2" fill="none"/></svg>We will facilitate &amp; oversee your development of better and more effective ways of increasing performance and improving effectiveness.</li>
  <li style="margin-top:20px"><svg viewBox="0 0 10 9"><path d="M1 5l3 3 5-7" stroke="var(--tick)" stroke-width="2" fill="none"/></svg>Generate potent, empowering emotional states within yourself at will, and eliminate negative and limiting emotions.</li>
  <li style="margin-top:20px"><svg viewBox="0 0 10 9"><path d="M1 5l3 3 5-7" stroke="var(--tick)" stroke-width="2" fill="none"/></svg>Tides Of Motion can help you achieve, maintain and enhance excellence.</li>
  <li style="margin-top:20px"><svg viewBox="0 0 10 9"><path d="M1 5l3 3 5-7" stroke="var(--tick)" stroke-width="2" fill="none"/></svg>Develop strong teamwork and relationships, foster positive interpersonal skills, negotiate and problem solve to create solution-oriented, win-win approaches, build deep levels of rapport, elicit and fulfil the criteria and values of clients.</li>
  <li style="margin-top:20px"><svg viewBox="0 0 10 9"><path d="M1 5l3 3 5-7" stroke="var(--tick)" stroke-width="2" fill="none"/></svg>We allow you to gain the emotional control over your life you've always wanted.</li>
</ul>

<div class="abs" style="left:342px;top:903px;width:80px;height:81px;background:linear-gradient(#a7713d,#4d9ab8)" role="img" aria-label="Photo of a student holding books"></div>
<h3 class="abs post-title" style="top:901px;font-weight:400">Lorem ipsum dolor sit amet,<br>consectetur adipisicing elit</h3>
<div class="abs meta" style="top:951px"><span><i></i>demoadmin</span><span><i></i>March 21, 2012</span><span><i></i>1</span></div>
<p class="abs post-text" style="top:971px">Sed ut perspiciatis unde omnis iste natus error sit voluptatem accusantium doloremque laudantium, totam rem aperiam, eaque ipsa quae ab illo inventore veritatis et quasi architecto beatae vitae di... <b style="font-weight:500">Read More »</b></p>

<div class="abs" style="left:342px;top:1032px;width:80px;height:80px;background:linear-gradient(135deg,#6b3b22,#c99a6a,#b6a4c9)" role="img" aria-label="Photo of colourful building blocks"></div>
<h3 class="abs post-title" style="top:1029px;font-weight:400">Sed ut perspiciatis unde</h3>
<div class="abs meta" style="top:1058px"><span><i></i>demoadmin</span><span><i></i>March 21, 2012</span><span><i></i>1</span></div>
<p class="abs post-text" style="top:1078px">Sed ut perspiciatis unde omnis iste natus error sit voluptatem accusantium doloremque laudantium, totam rem aperiam, eaque ipsa quae ab illo inventore veritatis et quasi architecto beatae vitae di... <b style="font-weight:500">Read More »</b></p>

<div class="abs pager"><span>Page 1 of 4</span><span class="on">1</span><span>2</span><span>3</span><span>4</span></div>

<footer class="abs footer">Copyright © 2013 Tides Of Motion All rights reserved.</footer>
</body>
</html>
```